Business Card Design Project

WE NEED A CARD WITH THE NAME AND LOGO IN ONE SIDE AND THE ODER JUST THE INFORMATIONS LIKE NAME, E-MAIL, PHONE AND SITE. I HAVE A IDEA OF THE CARD ALL BLACK AND JUST COLLOORS IN THE LOGO AND INFORMATIONS. WE WANT SANTHING SIMPLE AND ELEGANT. SAMETHING NEW WICTH PASS CONFIANCE.
Updates

I HAVE UP DATE THE INFORMATIONS OF WAHT WE NEED. THNKSĀ 

Target Market(s)

COMPANY WHO ORGANIZE BIG CORPORATIVE EVENTS.

Industry/Entity Type

Business

Requirements
Should not have
• MUCH INFORMATION.

```html
<!DOCTYPE html>
<html lang="en">
<head>
<meta charset="utf-8">
<title>Business Card – Front and Back</title>
<link rel="stylesheet" href="https://fonts.googleapis.com/css2?family=Orbitron:wght@700;900&family=Oswald:wght@400;500&family=Dosis:wght@500;600&display=swap">
<style>
  :root {
    --page-bg: #eceeee;
    --navy: #0f2240;
    --navy-deep: #0b1c36;
    --edge-blue: #1f5aa6;
    --bright-blue: #1a7ae6;
    --mid-blue: #0f5cc4;
    --dark-blue: #0a3e8c;
    --white: #ffffff;
    --soft-white: #e8eef8;
    --icon-blue: #7fb2ff;
  }
  * { margin: 0; padding: 0; box-sizing: border-box; }
  html, body { width: 1200px; height: 574px; overflow: hidden; }
  body { background: var(--page-bg); position: relative; font-family: "Dosis", sans-serif; }

  .card {
    position: absolute;
    left: 380px;
    width: 440px;
    height: 242px;
    border-radius: 24px;
    border: 2px solid var(--edge-blue);
    overflow: hidden;
    background: var(--navy);
  }
  .card--front { top: 30px; }
  .card--back { top: 302px; background: var(--navy-deep); }

  /* Front */
  .front-header {
    position: absolute; left: 0; top: 0; width: 100%; height: 132px;
    background: linear-gradient(115deg, var(--dark-blue) 0%, var(--mid-blue) 30%, var(--bright-blue) 50%, var(--mid-blue) 72%, var(--dark-blue) 100%);
    text-align: center;
  }
  .person-name {
    position: absolute; left: 0; right: 0; top: 44px;
    font-family: "Orbitron", sans-serif; font-weight: 900; font-size: 28px;
    letter-spacing: 4px; color: var(--white);
    -webkit-text-stroke: 0.6px var(--dark-blue);
  }
  .person-position {
    position: absolute; left: 0; right: 0; top: 78px;
    font-family: "Oswald", sans-serif; font-weight: 500; font-size: 21px;
    color: var(--white);
  }
  .front-details { position: absolute; left: 0; top: 132px; width: 100%; height: 110px; }
  .org-block { position: absolute; left: 30px; top: 20px; color: var(--soft-white); }
  .org-title { font-family: "Oswald", sans-serif; font-size: 14px; font-weight: 500; margin-bottom: 4px; }
  .address { position: relative; padding-left: 12px; font-size: 10.5px; line-height: 11px; }
  .address .pin { position: absolute; left: 0; top: 0; }
  .contact-list { position: absolute; left: 286px; top: 14px; list-style: none; color: var(--soft-white); font-size: 11px; }
  .contact-list li { display: flex; align-items: center; height: 20px; margin-bottom: 1px; }
  .contact-list svg { width: 12px; height: 12px; margin-right: 8px; }

  /* Back */
  .org-wordmark {
    position: absolute; left: 0; right: 0; top: 86px; text-align: center;
    font-family: "Orbitron", sans-serif; font-weight: 900; font-size: 30px;
    letter-spacing: 2px; color: var(--white);
    -webkit-text-stroke: 0.6px var(--navy);
  }
  .website {
    position: absolute; left: 0; right: 0; top: 140px; text-align: center;
    font-family: "Dosis", sans-serif; font-weight: 600; font-size: 14px; color: var(--white);
  }
</style>
</head>
<body>
  <section class="card card--front" aria-label="Card front">
    <header class="front-header">
      <h1 class="person-name">NAME</h1>
      <p class="person-position">Position</p>
    </header>
    <div class="front-details">
      <div class="org-block">
        <p class="org-title">Organization Name</p>
        <div class="address">
          <svg class="pin" width="8" height="10" viewBox="0 0 8 10"><path d="M4 0a3 3 0 0 1 3 3c0 2-3 5-3 5S1 5 1 3a3 3 0 0 1 3-3z" fill="var(--icon-blue)"/><line x1="1" y1="9.5" x2="7" y2="9.5" stroke="var(--icon-blue)"/></svg>
          Address line 1<br>Address line 2<br>Address line 3
        </div>
      </div>
      <ul class="contact-list">
        <li><svg viewBox="0 0 12 12"><path d="M4 1 C1 3 1 9 4 11 L5.5 9.5 L4.5 7.5 L3.6 7.8 C3 6.5 3 5.5 3.6 4.2 L4.5 4.5 L5.5 2.5 Z" fill="var(--icon-blue)"/></svg>1234567890</li>
        <li><svg viewBox="0 0 12 12"><rect x="3" y="0.5" width="6" height="11" rx="1" fill="var(--white)"/><rect x="4" y="2" width="4" height="7" fill="var(--navy)"/></svg>1234567890</li>
        <li><svg viewBox="0 0 12 12"><path d="M1 5 L6 2 L11 5 V11 H1 Z" fill="var(--icon-blue)"/><path d="M1 5 L6 8 L11 5" fill="none" stroke="var(--white)" stroke-width="1"/></svg>abc@xyz.com</li>
      </ul>
    </div>
  </section>

  <section class="card card--back" aria-label="Card back">
    <h2 class="org-wordmark">ORGANIZATION NAME</h2>
    <p class="website">www.xyz.com</p>
  </section>
</body>
</html>
```